Crestline Venture Partners Business Card Redesign Project

CRESTLINE VENTURE PARTNERS
Our company needs to have its business cards redesigned as the current design no longer reflects the business brand or attracts the type of clientele we are seeking.

MUST LOOK
★ Upmarket
★ Reflect Quality
★ Corporate feel
★ Professional
★ Innovative
★ Colourful

MUST PROMOTE
★ Market Leader
★ Knowledge
★ Expertise
★ Experience
★ Solutions
★ Advice

MUST FEEL
★ Classy
★ Elegant
★ Savvy
★ Edgy
★ Upbeat

WHAT WE DO
Crestline Venture Partners provides project management and project controls consultancy services to companies in many industry sectors, within Australia and overseas. My company has developed a business brand through forging strong business relationships within industry. We provide innovative tools, concepts and solutions to management teams to assist them in better plan and managing there project portfolios.

SECTORS OF INDUSTRY WE SERVICE
★Oil & Gas
★Minerals & Metals
★Petrochemical
★Manufacturing
★Building & Construction
★Telecommunications
★Rail
★Civil

BUSINESS CARD DETAILS REQUIRED ON FRONT
Marcus Delane
Business Owner
Tel: 0438519627
Email: marcusdelane@crestlineventurepartners.com
Website: www.crestlineventurepartners.com.au

BUSINESS CARD DETAILS REQUIRED ON BACK
Insight | Strategy | Delivery | Results

ATTACHMENTS

Target Market(s)

Oil & Gas I Mining & Resources I Industry in General
Upmarket Clientele
Corporate World

Industry/Entity Type

Industry

Requirements
Must have
• Must be creative and a unique design
The business card must have information on the front and back

```html
<!DOCTYPE html>
<html lang="en">
<head>
<meta charset="utf-8">
<title>Crestline Venture Partners – Business Card</title>
<link rel="stylesheet" href="https://fonts.googleapis.com/css2?family=Montserrat:wght@400;500;700;800&display=swap">
<style>
  :root {
    --page-bg: #e9e9eb;
    --brand-red: #d6001c;
    --brand-red-deep: #b80018;
    --ink: #1c1c1e;
    --ink-soft: #3a3a3c;
    --card-white: #ffffff;
    --card-grey: #ececec;
    --skyline: #141414;
  }
  * { box-sizing: border-box; margin: 0; padding: 0; }
  html, body { width: 1200px; height: 900px; overflow: hidden; }
  body {
    background: var(--page-bg);
    font-family: "Montserrat", Arial, sans-serif;
    color: var(--ink);
    position: relative;
  }
  .card {
    position: absolute;
    left: 250px;
    width: 700px;
    height: 400px;
    border-radius: 26px;
    overflow: hidden;
    box-shadow: 0 10px 28px rgba(0,0,0,0.18);
  }

  /* ---------- Back ---------- */
  .card-back {
    top: 30px;
    background: linear-gradient(160deg, var(--brand-red) 0%, var(--brand-red-deep) 100%);
    color: var(--card-white);
  }
  .brand {
    position: absolute;
    display: flex;
    align-items: center;
    gap: 16px;
  }
  .card-back .brand { left: 60px; top: 160px; }
  .brand-mark {
    width: 46px;
    height: 46px;
    flex: none;
  }
  .card-back .brand-mark { background: var(--card-white); }
  .brand-name {
    font-weight: 800;
    font-size: 30px;
    letter-spacing: 0.5px;
    line-height: 1;
    white-space: nowrap;
  }
  .tagline {
    position: absolute;
    font-size: 13px;
    white-space: nowrap;
  }
  .card-back .tagline {
    left: 122px;
    top: 202px;
    font-weight: 500;
  }
  .skyline-band {
    position: absolute;
    left: 0;
    right: 0;
    bottom: 0;
    height: 70px;
    background: var(--skyline);
  }
  .values {
    position: absolute;
    right: 40px;
    bottom: 25px;
    font-size: 13px;
    font-weight: 500;
    letter-spacing: 1.5px;
    color: var(--card-white);
    white-space: nowrap;
  }

  /* ---------- Front ---------- */
  .card-front {
    top: 470px;
    background: radial-gradient(ellipse at 40% 30%, var(--card-white) 0%, var(--card-grey) 100%);
  }
  .card-front .brand { left: 56px; top: 50px; }
  .card-front .brand-mark { background: var(--brand-red); }
  .card-front .brand-name { color: var(--ink); font-size: 31px; }
  .card-front .tagline {
    left: 118px;
    top: 94px;
    font-weight: 700;
    color: var(--ink);
  }
  .holder {
    position: absolute;
    left: 140px;
    top: 140px;
  }
  .holder-name {
    font-size: 26px;
    font-weight: 400;
    line-height: 1.2;
    color: var(--brand-red);
  }
  .holder-role {
    font-size: 17px;
    font-weight: 400;
    color: var(--ink-soft);
    margin-top: 2px;
  }
  .contact-list {
    position: absolute;
    left: 140px;
    top: 230px;
    list-style: none;
  }
  .contact-list li {
    display: flex;
    align-items: center;
    gap: 12px;
    font-size: 15.5px;
    color: var(--ink-soft);
    height: 32px;
    white-space: nowrap;
  }
  .contact-icon {
    width: 20px;
    height: 20px;
    flex: none;
  }
  .social-row {
    position: absolute;
    left: 50px;
    bottom: 40px;
    display: flex;
    gap: 6px;
  }
  .social-row span {
    width: 22px;
    height: 22px;
    background: var(--brand-red);
    border-radius: 3px;
  }
</style>
</head>
<body>

  <section class="card card-back" aria-label="Card back">
    <div class="brand">
      <span class="brand-mark"></span>
      <span class="brand-name">CRESTLINE VENTURE PARTNERS</span>
    </div>
    <p class="tagline">Delivering Clear Project Controls and Portfolio Guidance</p>
    <div class="skyline-band" role="img" aria-label="Silhouette of an industrial skyline with cranes"></div>
    <p class="values">INSIGHT | STRATEGY | DELIVERY | RESULTS</p>
  </section>

  <section class="card card-front" aria-label="Card front">
    <div class="brand">
      <span class="brand-mark"></span>
      <span class="brand-name">CRESTLINE VENTURE PARTNERS</span>
    </div>
    <p class="tagline">Delivering Clear Project Controls and Portfolio Guidance</p>

    <div class="holder">
      <p class="holder-name">Marcus Delane</p>
      <p class="holder-role">Business Owner</p>
    </div>

    <ul class="contact-list">
      <li>
        <svg class="contact-icon" viewBox="0 0 20 20" aria-hidden="true">
          <circle cx="10" cy="10" r="10" fill="var(--brand-red)"/>
          <path d="M6 7 Q6 5 8 5 L9 7 L8 8 Q9 11 12 12 L13 11 L15 12 Q15 14 13 14 Q7 13 6 7 Z" fill="#fff"/>
        </svg>
        <span>0438 519 627</span>
      </li>
      <li>
        <svg class="contact-icon" viewBox="0 0 20 20" aria-hidden="true">
          <circle cx="10" cy="10" r="10" fill="var(--brand-red)"/>
          <rect x="5" y="6.5" width="10" height="7" fill="#fff"/>
          <path d="M5 6.5 L10 10.5 L15 6.5" fill="none" stroke="var(--brand-red)" stroke-width="1"/>
        </svg>
        <span>marcusdelane@crestlineventurepartners.com</span>
      </li>
      <li>
        <svg class="contact-icon" viewBox="0 0 20 20" aria-hidden="true">
          <circle cx="10" cy="10" r="10" fill="var(--brand-red)"/>
          <g fill="none" stroke="#fff" stroke-width="1.1">
            <circle cx="10" cy="10" r="5.5"/>
            <ellipse cx="10" cy="10" rx="2.3" ry="5.5"/>
            <line x1="4.5" y1="10" x2="15.5" y2="10"/>
          </g>
        </svg>
        <span>www.crestlineventurepartners.com.au</span>
      </li>
    </ul>

    <div class="social-row" aria-label="Social profiles">
      <span></span><span></span><span></span>
    </div>
  </section>

</body>
</html>
```